Web Design for Solar Energy Consultancy Company

~ May 3, 2017 Update ~
As our project is rapidly progressing towards its completion, we started building up the list of designs that attracted the most of the team's attention. Additional submittals are still most welcome. Before submitting your proposal, however, we can recommend to review the concepts that received 4 stars as these are the ones that, in our opinion, most closely match the brief's requirements. Thank you!!
~ April 30, 2017 Update ~
The project deadline has been extended to attract a broader design community and to better tailor the final design to the requirements of the project.
A "light", "clean" (minimalistic), professionally looking, unique design is expected. Please, try to avoid industry cliches. Also, please use green, which became another industry cliche, with great caution. The brief provides minimum details to foster creativity. With the same notion in mind, the page content information is not provided.
Thank you for your feedback and support of the project!!
~ April 22, 2017 Update ~
Additional comments after starting receiving more designs:
- your attention to the brief's requirements will be highly appreciated. It is expected that the design is unique - standard, commonly used, images, formats and approaches do not fall under this category. There is no need to "bombard" with slightly different variations of the same design. It is expected that a conceptual (preliminary) design is submitted first, and, after it is reviewed (each design will receive a star rating and, if the star rating is greater than 3, a detailed feedback), the requested changes are implemented. We believe this will allow to approach the design process more efficiently and safe additional time to both the Designers's Community and our company. Thank you for understanding.
Clarification, please submit two variations of a design:
1) 1 page "business card" design that the company will be able to use during its startup stage;
2) the fully functional design (as per the requirements outlined below) for the company to transition to after the start-up period is over. Same design principles as developed for option 1 should be used for this variation.
Additional clarification, please note that the news block will not require images (at least during the start-up stage). It is envisioned to be a news feeder.
~ April 21, 2017 Update ~
Preliminary comments after receiving first designs:
- please try to create a unique design, using common elements wisely. Though such solar energy "attributes" as a solar panel or a bulb are very well recognized and allow quickly identify the nature of the business, they also became so common that in many cases a design may seem very similar to the one of others (Oh!, I've already seen this... effect).
- please try to introduce the company's logo unobtrusively. The size and position of the logo should clearly identify the company, but the message should be subtle, the logo should not distract from the main design. Brask's swoosh did not need to occupy have the screen.
- please use the green color with caution as it was with the company's logo. True, it is a green energy. But there is no need for the color to "scream" about it. Use the amount of green and its tone (avoid acid green) wisely.
--------------------------------------------------------------------------------
1. Main Goal
Develop a website that can represent the company to the industry stakeholders and become its "business card" during the start-up stage.
2. Secondary Goal
Develop a structure of a fully functional website that the "business card" design can eventually be transformed to staying consistent with the original design principles.
3. Key Audience
Varolu Corp. is providing consulting and technical services in the area of Solar Energy. The industry stakeholders include project developers, financial community, governmental bodies, OEMs, and competition.
4. Site Map
- HOME
• About
• Services
• Solar Energy
• News
• Contacts
• Social Media
- SERVICES*
- PROJECTS*
- FINANCE*
- TRAINING*
- SOLAR (ENERGY)*
* Maybe inactive / partially functional during the start-up stage.
5. Technical Specifications
Online brochure website during the start-up stage with a capability to be eventually transformed to a fully functional website while preserving the original design principles.
The design to be appealing, "light", professional, and with an intuitive and easy to navigate interface. Modern coding principles supporting efficiency and security to be utilized. Newest industry trends in website coding will be welcome.
The website to be designed so that it would fit well a computer, tablet, or mobile phone screen of any size. Cross-platform functionality to be taken into consideration to ensure that the website is fully functional on any platform.
Company's logo has already been designed and will be shared with the short-listed designers during the final design stage.
6. Interaction
The website will provide information about the company, our services, and projects. In addition, the industry insight, accumulated knowledge, and most recent trends are planned to be shared with stakeholders and attract and retain the audience.
Interaction with designers during the website development is envisioned to go through the following steps:
a) conceptual design - to be proposed by a designer originally. All conceptual designs will be reviewed and a feedback provided to pre-selected designers;
b) (preliminary and) final design - depending on the level of additional changes required can be broken into two steps. After discussing preliminary designs, company images will be provided to the selected finalists, who will compete with their final proposals.
7. Industry Stakeholders
- https://www.quellbrin.com/power/solar-power.- http://www.pakortavon.com/
- http://www.vellitrazo.com/about/company/
- https://www.oruxem.com/energy/index.html
8. Budget
Defined by the project.
9. Timescale
Defined by the project.
12. Additional Info
- No copy-cats, standard graphics, or cliches please!
- Additional information / clarifications will be gladly provided upon request.
- This specification may be updated throughout the project to reflect discussions with / changes proposed by the Designers community.

```html
<!DOCTYPE html>
<html lang="en">
<head>
<meta charset="utf-8">
<title>Varolu Corp — Renewable Energy</title>
<link href="https://fonts.googleapis.com/css2?family=Roboto:wght@400;500;700&family=Roboto+Condensed:wght@700&family=Exo+2:wght@600;700&family=Roboto+Slab:wght@400&display=swap" rel="stylesheet">
<style>
:root{
  --orange:#f7a000;
  --orange-light:#ffc21a;
  --orange-dark:#f08c00;
  --ink:#111111;
  --text:#555555;
  --muted:#777777;
  --green:#4c8f24;
  --white:#ffffff;
  --rule:#e3e3e3;
}
*{margin:0;padding:0;box-sizing:border-box}
html,body{width:1200px;height:2250px;overflow:hidden;background:var(--white)}
body{font-family:"Roboto",Arial,sans-serif;color:var(--text);position:relative}
.abs{position:absolute}
.photo{position:absolute}

/* hero */
.hero{position:absolute;left:0;top:0;width:1200px;height:590px;overflow:hidden}
.hero-photo-worker{left:0;top:0;width:660px;height:590px;
  clip-path:polygon(0 225px,225px 0,405px 0,645px 590px,0 590px);
  background:linear-gradient(160deg,#7ea55a 0%,#4f6d8f 35%,#2f4e8c 60%,#5b6f8c 100%)}
.hero-photo-sky{left:885px;top:0;width:315px;height:375px;
  clip-path:polygon(0 0,100% 0,100% 100%);
  background:radial-gradient(circle at 55% 30%,#ffd23a 0,#ff9d00 70px,#e8e4d8 72px,#cfd7de 100%)}
.hero-photo-panels{left:547px;top:262px;width:436px;height:436px;border-radius:50%;border:5px solid var(--white);
  background:linear-gradient(170deg,#e9eef3 0%,#e9eef3 25%,#2b3f75 45%,#34508f 65%,#6e9a3f 80%,#4f7f2a 100%)}
.hero-line{left:0;top:0}
.logo{left:523px;top:52px;display:flex;align-items:center;gap:10px}
.logo-mark{width:58px;height:58px;border-radius:50%;background:var(--orange)}
.logo-name{font-family:"Roboto",Arial,sans-serif;font-weight:500;font-size:34px;letter-spacing:3px;color:#333333}
.hero-title{left:380px;width:540px;top:162px;text-align:center;font-family:"Roboto Condensed",Arial,sans-serif;font-weight:700;font-size:37px;line-height:46px;color:var(--ink)}
.btn{display:flex;align-items:center;justify-content:center;border-radius:28px;
  background:linear-gradient(180deg,var(--orange-light),var(--orange-dark));color:var(--ink);font-size:19px;font-weight:400;text-decoration:none}
.hero-btn{left:567px;top:266px;width:198px;height:53px}

/* nav */
.nav{left:0;top:590px;width:1200px;height:52px;background:linear-gradient(180deg,var(--orange-light),var(--orange-dark));border-top:2px solid #ffd86a}
.nav a{position:absolute;top:16px;transform:translateX(-50%);font-size:17px;color:var(--ink);text-decoration:none;white-space:nowrap}
.nav a.active{color:var(--white)}

/* section headings */
.heading{font-family:"Exo 2",Arial,sans-serif;font-weight:700;color:var(--ink);font-size:39px;text-align:center;position:absolute}

/* welcome */
.welcome-photo-kit{left:0;top:832px;width:315px;height:218px;
  clip-path:polygon(0 15px,80% 0,100% 70%,55% 100%,0 95%);
  background:linear-gradient(150deg,#1c2333 0%,#2c3850 50%,#c9ccd1 100%)}
.welcome-photo-wind{left:804px;top:645px;width:396px;height:795px;
  clip-path:polygon(100% 0,0 390px,100% 100%);
  background:linear-gradient(180deg,#b9c8d6 0%,#8aa3b8 40%,#6b8e4e 70%,#3d6a2f 100%)}
.welcome-text{left:215px;top:758px;width:780px;text-align:center;font-size:14px;line-height:23px;color:var(--text)}
.welcome-btn{left:502px;top:866px;width:198px;height:53px}

/* services */
.service{position:absolute;top:1160px;width:235px}
.service-head{display:flex;align-items:center;gap:10px;height:50px}
.service-title{font-family:"Exo 2",Arial,sans-serif;font-weight:700;font-size:18px;color:var(--ink)}
.service-title.accent{color:var(--orange)}
.service-text{margin-top:12px;font-size:14px;line-height:21px;color:var(--text)}
.service-link{display:inline-block;margin-top:16px;font-size:14px;color:var(--ink);text-decoration:underline}
.service-link.accent{color:var(--orange)}

/* testimonial */
.testi-photo-sky{left:0;top:1302px;width:440px;height:873px;
  clip-path:polygon(0 0,100% 50%,0 100%);
  background:linear-gradient(180deg,#2c7fe0 0%,#6fb1f0 35%,#3f74c9 58%,#7bbf3c 75%,#4d9427 100%)}
.testi-photo-bulb{left:1080px;top:1530px;width:120px;height:390px;
  clip-path:polygon(35% 10%,100% 5%,100% 72%,70% 72%,70% 100%,48% 100%,48% 72%,35% 60%,28% 35%);
  background:linear-gradient(180deg,#d7ecf7 0%,#3aa4e0 40%,#1368b8 65%,#b7bcc2 80%,#808488 100%)}
.quote{position:absolute;top:1470px;width:330px}
.quote-mark{position:absolute;left:0;top:0;font-family:Georgia,serif;font-size:70px;line-height:60px;color:#cfcfcf}
.quote-text{margin-left:40px;font-size:14px;line-height:23px;color:var(--text)}
.quote-author{margin-left:38px;margin-top:12px;font-family:"Roboto Slab",Georgia,serif;font-size:19px;color:var(--orange)}

/* contact */
.col-title{position:absolute;top:1880px;font-size:21px;color:var(--green)}
.detail{position:absolute;left:338px;display:flex;gap:12px;font-size:14px;line-height:22px;color:var(--text)}
.detail strong{font-weight:500;color:#333333}
.news{position:absolute;left:702px;width:390px}
.news-text{font-size:15px;line-height:24px;color:#333333}
.news-date{display:flex;align-items:center;gap:4px;font-size:13px;color:var(--muted);margin-top:2px}
.view-all{left:1006px;top:2078px;font-size:18px;color:var(--orange);text-decoration:underline}

/* footer */
.footer{left:0;top:2175px;width:1200px;height:75px;background:linear-gradient(180deg,var(--orange-light),var(--orange-dark))}
.copyright{left:78px;top:28px;font-size:13px;font-weight:700;color:var(--ink)}
.copyright span{color:var(--white)}
.social{position:absolute;top:18px;width:39px;height:39px;border-radius:50%;border:2px solid var(--white)}
.social.first{background:var(--white)}
</style>
</head>
<body>

<header class="hero">
  <div class="photo hero-photo-worker" role="img" aria-label="Technician inspecting a row of solar panels in a field"></div>
  <div class="photo hero-photo-sky" role="img" aria-label="Bright sun over a cloudy sky and yellow field"></div>
  <div class="photo hero-photo-panels" role="img" aria-label="Ground mounted solar panels on green grass"></div>
  <svg class="abs hero-line" width="1200" height="590" viewBox="0 0 1200 590" aria-hidden="true">
    <line x1="0" y1="225" x2="225" y2="0" stroke="#9abf5a" stroke-width="3"/>
    <line x1="870" y1="0" x2="1200" y2="360" stroke="#d9d9d9" stroke-width="3"/>
  </svg>
  <div class="abs logo"><span class="logo-mark"></span><span class="logo-name">VAROLU CORP</span></div>
  <h1 class="abs hero-title">DEVELOPING RENEWABLE<br>ENERGY PROJECT</h1>
  <a class="abs btn hero-btn" href="#contact">Contact Us Now</a>
</header>

<nav class="abs nav">
  <a class="active" href="#" style="left:167px">Home</a>
  <a href="#" style="left:307px">About Us</a>
  <a href="#" style="left:456px">Services</a>
  <a href="#" style="left:598px">Projects</a>
  <a href="#" style="left:744px">Training</a>
  <a href="#" style="left:873px">News</a>
  <a href="#" style="left:1010px">Contact Us</a>
</nav>

<section class="welcome">
  <div class="photo welcome-photo-kit" role="img" aria-label="Portable folding solar panel kit"></div>
  <div class="photo welcome-photo-wind" role="img" aria-label="Offshore wind turbines along a grassy coastline"></div>
  <h2 class="heading" style="left:300px;width:600px;top:688px">Welcome To Varolu Corp</h2>
  <p class="abs welcome-text">Lorem Ipsum is simply dummy text of the printing and typesetting industry. Lorem Ipsum has been the industry's standard dummy text ever since the 1500s, when an unknown printer took a galley of type and scrambled it to make a type specimen book.Lorem Ipsum is simply dummy text of the printing and typesetting industry. Lorem Ipsum has been the industry's standard dummy text.</p>
  <a class="abs btn welcome-btn" href="#">Read More</a>
</section>

<section class="services">
  <h2 class="heading" style="left:240px;width:400px;top:1068px">Our Services</h2>

  <div class="service" style="left:78px">
    <div class="service-head">
      <svg width="62" height="50" viewBox="0 0 62 50" aria-hidden="true">
        <path d="M8 4h46l6 28H2z" fill="#2f8a3c"/>
        <path d="M5 18h52M20 4l-3 28M31 4v28M42 4l3 28" stroke="#fff" stroke-width="2"/>
        <rect x="28" y="32" width="6" height="11" fill="#2f8a3c"/>
        <rect x="16" y="43" width="30" height="5" fill="#2f8a3c"/>
      </svg>
      <span class="service-title accent">Solar Energy</span>
    </div>
    <p class="service-text">Lorem Ipsum is simply dummy text of the printing and type setting industry.</p>
    <a class="service-link accent" href="#">READ MORE »</a>
  </div>

  <div class="service" style="left:325px">
    <div class="service-head">
      <svg width="50" height="50" viewBox="0 0 50 50" aria-hidden="true">
        <rect x="10" y="8" width="28" height="40" rx="3" fill="#2f8a3c"/>
        <rect x="18" y="3" width="12" height="6" fill="#2f8a3c"/>
        <path d="M26 16l-7 13h6l-3 12 9-16h-6l3-9z" fill="#fff"/>
        <path d="M2 18h6M1 26h7M2 34h6M42 18h6M42 26h7M42 34h6" stroke="#f7a000" stroke-width="2.5"/>
      </svg>
      <span class="service-title">Finance</span>
    </div>
    <p class="service-text">Lorem Ipsum is simply dummy text of the printing and type setting industry.</p>
    <a class="service-link" href="#">READ MORE »</a>
  </div>

  <div class="service" style="left:571px">
    <div class="service-head">
      <svg width="46" height="54" viewBox="0 0 46 54" aria-hidden="true">
        <path d="M20 14C10 0 2 8 4 14c6 2 12 2 16 0z" fill="#2f8a3c"/>
        <path d="M24 12C32 -2 44 4 42 12c-6 3-13 3-18 0z" fill="#5aab2f"/>
        <rect x="11" y="18" width="24" height="16" rx="3" fill="#2f8a3c"/>
        <rect x="15" y="13" width="3" height="6" fill="#2f8a3c"/>
        <rect x="28" y="13" width="3" height="6" fill="#2f8a3c"/>
        <path d="M23 34v8c0 6-8 6-8 10" stroke="#2f8a3c" stroke-width="3" fill="none"/>
      </svg>
      <span class="service-title">Training</span>
    </div>
    <p class="service-text">Lorem Ipsum is simply dummy text of the printing and type setting industry.</p>
    <a class="service-link" href="#">READ MORE »</a>
  </div>
</section>

<section class="testimonial">
  <div class="photo testi-photo-sky" role="img" aria-label="Solar panels on a green meadow under a blue sky"></div>
  <div class="photo testi-photo-bulb" role="img" aria-label="Light bulb holding a miniature landscape with a solar panel"></div>
  <h2 class="heading" style="left:535px;width:400px;top:1390px">Testimonial</h2>

  <div class="quote" style="left:350px">
    <span class="quote-mark">"</span>
    <p class="quote-text">"Lorem Ipsum is simply dummy text of the printing and typesetting industry. Lorem Ipsum has been the industry standard dummy.Lorem Ipsum is simply dummy text of the printing and typesetting industry."</p>
    <p class="quote-author">- Elena Marwick</p>
  </div>
  <div class="quote" style="left:768px">
    <span class="quote-mark">"</span>
    <p class="quote-text">"Lorem Ipsum is simply dummy text of the printing and typesetting industry. Lorem Ipsum has been the industry standard dummy.Lorem Ipsum is simply dummy text of the printing and typesetting industry."</p>
    <p class="quote-author">- Elena Marwick</p>
  </div>
</section>

<section class="contact" id="contact">
  <h2 class="heading" style="left:500px;width:425px;top:1780px">Get in Touch</h2>

  <h3 class="col-title" style="left:338px;font-weight:400">Company Detail</h3>
  <div class="detail" style="top:1922px">
    <svg width="20" height="24" viewBox="0 0 20 24" aria-hidden="true"><path d="M10 2a7 7 0 0 0-7 7c0 6 7 13 7 13s7-7 7-13a7 7 0 0 0-7-7z" fill="none" stroke="#888" stroke-width="1.5"/><circle cx="10" cy="9" r="2.5" fill="none" stroke="#888" stroke-width="1.5"/></svg>
    <p><strong>VAROLU Corp</strong><br>123,Lorem ipsum dummy &nbsp;text,<br>Country,123456.</p>
  </div>
  <div class="detail" style="top:2016px">
    <svg width="22" height="22" viewBox="0 0 22 22" aria-hidden="true"><path d="M5 2l4 4-2 3c1 3 3 5 6 6l3-2 4 4-3 3C9 20 2 13 2 5z" fill="none" stroke="#888" stroke-width="1.5"/></svg>
    <p>+123 456 7878</p>
  </div>
  <div class="detail" style="top:2058px;gap:4px">
    <svg width="22" height="22" viewBox="0 0 22 22" aria-hidden="true"><rect x="1" y="5" width="20" height="13" fill="none" stroke="#888" stroke-width="1.5"/><path d="M1 5l10 8 10-8" fill="none" stroke="#888" stroke-width="1.5"/></svg>
    <p>varolugroup@helivantmail.com</p>
  </div>

  <h3 class="col-title" style="left:702px;font-weight:400">Latest News</h3>
  <div class="news" style="top:1926px">
    <p class="news-text">Lorem Ipsum is simply dummy text of the printing and typesetting industry.</p>
    <p class="news-date"><svg width="15" height="15" viewBox="0 0 15 15" aria-hidden="true"><rect x="1" y="3" width="13" height="11" fill="none" stroke="#aaa"/><path d="M1 6h13M4 1v3M11 1v3" stroke="#aaa"/></svg>15 April, 2017</p>
  </div>
  <div class="news" style="top:2010px">
    <p class="news-text">Lorem Ipsum is simply dummy text of the printing and typesetting industry.</p>
    <p class="news-date"><svg width="15" height="15" viewBox="0 0 15 15" aria-hidden="true"><rect x="1" y="3" width="13" height="11" fill="none" stroke="#aaa"/><path d="M1 6h13M4 1v3M11 1v3" stroke="#aaa"/></svg>10 April 2017</p>
  </div>
  <a class="abs view-all" href="#">View All</a>
</section>

<footer class="abs footer">
  <p class="abs copyright">© 2017 &nbsp;<span>VAROLU CORP,</span>&nbsp; All rights reserved.</p>
  <a class="social first" href="#" aria-label="Social profile 1" style="left:874px"></a>
  <a class="social" href="#" aria-label="Social profile 2" style="left:922px"></a>
  <a class="social" href="#" aria-label="Social profile 3" style="left:973px"></a>
  <a class="social" href="#" aria-label="Social profile 4" style="left:1027px"></a>
  <a class="social" href="#" aria-label="Social profile 5" style="left:1075px"></a>
</footer>

</body>
</html>
```